Business card for a young woman who performs life enhancement activities with people who have developmental disabilities, what used to be called retardation. She wants to focus on the creative part of her work. She has a degree in art and will engage clients in art projects as well as helping them learn to do things like grocery shop, cook meals, set goals, and live independently.

Target Market(s)

Parents, caregivers, guardians, relatives of people with developmental disabilities, meaning they have not developed in their mental capacities.

Industry/Entity Type

Business

Contact Information for Business Card

Bright Path Care Studio, Marisa J. Tolliver, 417 263-9184, marisa@marisatolliver.example, Life enhancement services for people with developmental disabilities. No address.

Font styles to use
Serif

Requirements
Must have
• Marisa wants it to have some indication of the art or creative part of her work with clients. But it must also be businesslike so it appeals to the parents. They have to see her as a professional, but she's compassionate and artsy. She wants just her company name on the front. The other information should be on the back.

```html
<!DOCTYPE html>
<html lang="en">
<head>
<meta charset="utf-8">
<title>Bright Path Care Studio – Business Card</title>
<link rel="stylesheet" href="https://fonts.googleapis.com/css2?family=Arimo:wght@400;700&display=swap">
<style>
  :root {
    --backdrop: #4b4b4b;
    --card: #ffffff;
    --ink: #333333;
    --navy: #2b2f7e;
    --rule: #3a3a3a;
    --spectrum: linear-gradient(90deg, #e8462a 0%, #f39a26 10%, #f4e41c 22%, #6cbf4b 38%, #5fc7d9 55%, #2f55a4 70%, #6b3f98 82%, #c2408f 92%, #e0263a 100%);
  }
  * { box-sizing: border-box; margin: 0; padding: 0; }
  html, body { width: 1200px; height: 1000px; overflow: hidden; }
  body {
    position: relative;
    background: var(--backdrop);
    font-family: "Arimo", Arial, sans-serif;
    color: var(--ink);
  }
  .card {
    position: absolute;
    background: var(--card);
    overflow: hidden;
  }
  .card-front { left: 198px; top: 140px; width: 578px; height: 338px; }
  .card-back  { left: 437px; top: 538px; width: 583px; height: 342px; }
  .spectrum-band {
    position: absolute; left: 0; right: 0; bottom: 0; height: 17px;
    background: var(--spectrum);
  }
  .company-name {
    position: absolute; left: 0; right: 0; top: 80px;
    text-align: center;
    font-size: 44px; font-weight: 700; line-height: 1.1;
    color: var(--navy);
  }
  .tagline {
    position: absolute; left: 0; width: 578px; top: 235px;
    text-align: center;
    font-size: 17px; line-height: 22px;
  }
  .portrait-frame {
    position: absolute; left: 46px; top: 93px; width: 148px; height: 144px;
    padding: 2px; background: var(--spectrum);
  }
  .portrait {
    width: 100%; height: 100%;
    background: linear-gradient(160deg, #e2d3a8 0%, #b89c7a 45%, #6f5a4e 100%);
  }
  .contact {
    position: absolute; left: 206px; top: 98px; width: 323px;
  }
  .person-name {
    text-align: center; font-size: 32px; letter-spacing: 0.5px;
    line-height: 38px; padding-left: 12px;
  }
  .rule { height: 3px; background: var(--rule); }
  .contact-line { font-size: 17px; line-height: 37px; }
  .contact-phone { text-align: center; padding-left: 20px; }
  .contact-email { padding-left: 29px; }
</style>
</head>
<body>
  <section class="card card-front">
    <h1 class="company-name">Bright Path<br>Care Studio</h1>
    <p class="tagline">Life Enhancement Services for people with<br>Developmental Disabilities</p>
    <div class="spectrum-band"></div>
  </section>

  <section class="card card-back">
    <div class="portrait-frame">
      <div class="portrait" role="img" aria-label="Portrait photo of Marisa with a client"></div>
    </div>
    <div class="contact">
      <h2 class="person-name">MARISA J. TOLLIVER</h2>
      <div class="rule"></div>
      <p class="contact-line contact-phone">Phone: 417 263-9184</p>
      <div class="rule"></div>
      <p class="contact-line contact-email">Email: marisa@marisatolliver.example</p>
      <div class="rule"></div>
    </div>
    <div class="spectrum-band"></div>
  </section>
</body>
</html>
```